Autodetailing namecard design: Rose Gold Lettering on Black Matt

This is a namecard design project
requiring two-sided design
Base Color of Namecard: black matt

On front:
Company name,
"Lumen Finishes 47 Kelapa"
Subtext: Auto Detailing Studio

Name of card holder: Dennis Lowe
Phone Number: +6012-4837-5062
address: 47, Jalan Kelapa 3/5Taman Seri Kelapa, 81200 Johor Bahru, Johor, Malaysia

Back:
Our Services
High Gloss Car Paint Protection
Custom Color Modification and Styling
Anti-Chip Glass Protection Film
Heat Rejection Glass Tinting

Target Market(s)

Autodetailing for highend cars

Contact Information for Business Card

as mentioned in project details

Colors

Designer to choose colors to be used in the design.

Requirements
Must have
• The main value-add to this project is the design of a logo suited for our purpose and name, and the inclusion of business card details into the card design

```html
<!DOCTYPE html>
<html lang="en">
<head>
<meta charset="utf-8">
<title>Lumen Finishes 47 Kelapa – Business Card</title>
<link rel="stylesheet" href="https://fonts.googleapis.com/css2?family=Lato:wght@400;700&family=Roboto:wght@400&display=swap">
<style>
  :root {
    --stage: #1a1a1a;
    --card-front: #ffffff;
    --rose: #c9806a;
    --rose-light: #ecb7a9;
    --rose-mid: #dba08f;
    --rose-deep: #c98a76;
    --ink: #2e2e2e;
    --ink-dark: #111111;
    --divider: #b5b5b5;
  }
  * { margin: 0; padding: 0; box-sizing: border-box; }
  html, body {
    width: 1200px; height: 900px; overflow: hidden;
    background: var(--stage);
  }
  .canvas { position: relative; width: 1200px; height: 900px; }

  .card {
    position: absolute; top: 275px; width: 477px; height: 294px;
    box-shadow: 4px 4px 8px rgba(0,0,0,0.55);
  }
  .card--front {
    left: 120px;
    background: var(--card-front);
    border-radius: 0 52px 0 52px;
  }
  .card--back {
    left: 619px; top: 276px; height: 293px;
    border-radius: 52px 0 52px 0;
    background: linear-gradient(150deg, var(--rose-deep) 0%, var(--rose-light) 22%, var(--rose-mid) 55%, var(--rose-light) 72%, var(--rose-deep) 100%);
    background: linear-gradient(200deg, #c98a76 0%, #d9a291 30%, #ecb7a9 62%, #e6ad9e 78%, #cd8b77 100%);
  }

  .brand {
    position: absolute; left: 37px; top: 88px; width: 183px;
    text-align: center;
    font-family: "Lato", sans-serif; font-weight: 700; color: var(--rose);
    text-transform: uppercase; line-height: 1.15;
  }
  .brand__name { font-size: 21px; letter-spacing: 0.5px; }
  .brand__tagline {
    margin-top: 10px; padding-bottom: 5px;
    font-size: 13px; border-bottom: 2px solid var(--rose);
  }

  .divider {
    position: absolute; left: 248px; top: 92px; width: 1px; height: 110px;
    background: var(--divider);
  }

  .contact {
    position: absolute; left: 270px; top: 85px;
    font-family: "Lato", sans-serif; color: var(--ink);
  }
  .contact__name { font-size: 20px; font-weight: 700; color: var(--rose); line-height: 1.2; }
  .contact__phone { font-size: 13px; line-height: 17px; }
  .contact__address { margin-top: 9px; font-size: 13px; line-height: 17px; font-style: normal; }

  .services {
    position: absolute; left: 0; right: 0; top: 78px;
    text-align: center; font-family: "Roboto", sans-serif; color: var(--ink-dark);
  }
  .services__title { font-size: 20px; font-weight: 400; line-height: 26px; }
  .services__list { list-style: none; margin-top: 20px; font-size: 14px; line-height: 23px; }
</style>
</head>
<body>
<div class="canvas">
  <section class="card card--front">
    <div class="brand">
      <div class="brand__name">Lumen Finishes<br>47 Kelapa</div>
      <div class="brand__tagline">Auto Detailing Studio</div>
    </div>
    <div class="divider"></div>
    <div class="contact">
      <div class="contact__name">DENNIS LOWE</div>
      <div class="contact__phone">+6012-4837-5062</div>
      <address class="contact__address">
        47, Jalan Kelapa<br>
        3/5Taman Seri Kelapa,<br>
        81200 Johor Bahru<br>
        Johor, Malaysia
      </address>
    </div>
  </section>

  <section class="card card--back">
    <div class="services">
      <h2 class="services__title">OUR SERVICES</h2>
      <ul class="services__list">
        <li>HIGH GLOSS CAR PAINT PROTECTION</li>
        <li>CUSTOM COLOR MODIFICATION AND STYLING</li>
        <li>ANTI-CHIP GLASS PROTECTION FILM</li>
        <li>HEAT REJECTION GLASS TINTING</li>
      </ul>
    </div>
  </section>
</div>
</body>
</html>
```